2 Page Business Flyer for Finance Business

Need a two page flyer created for a finance business. Lots of text and needs to fit on two pages.

Corporate business/banking look and feel. Not too many large images. Lots of white space, clean design. Attached is color palette and the text contents of the flyer.

```html
<!DOCTYPE html>
<html lang="en">
<head>
<meta charset="utf-8">
<title>Vanilla Contracts – Two Page Flyer</title>
<link href="https://fonts.googleapis.com/css2?family=Titillium+Web:wght@300;400;600;700&display=swap" rel="stylesheet">
<style>
:root{
  --navy:#1b1d45;
  --navy-deep:#14163a;
  --purple:#5a4fa4;
  --purple-soft:#7b6fc0;
  --teal:#3fb6a0;
  --ink:#333;
  --muted:#ccd;
  --backdrop:#e7e8ec;
  --paper:#fff;
  --alert:#d9534f;
}
*{box-sizing:border-box;margin:0;padding:0}
html,body{width:1200px;height:848px;overflow:hidden;background:var(--backdrop);font-family:"Titillium Web",sans-serif;color:var(--ink)}
.page{position:absolute;top:80px;width:536px;height:692px;background:var(--paper);overflow:hidden}
.page--one{left:48px}
.page--two{left:607px}
.masthead{position:absolute;left:0;top:0;width:100%;background:var(--navy)}
.page--one .masthead{height:100px}
.page--two .masthead{height:58px}
.page-title{position:absolute;top:44px;left:0;width:100%;text-align:center;color:#fff;font-weight:300;font-size:23px;letter-spacing:.1px}
.accent{position:absolute;left:0;width:100%}
.hero{position:absolute;left:0;width:100%}
.page--one .hero{top:112px;height:136px;background:linear-gradient(100deg,#c9d4e6 0%,#e9eef6 35%,#8aa6d4 60%,#dfe6f2 100%)}
.page--two .hero{top:72px;height:100px;background:linear-gradient(90deg,#132a4a 0%,#1f4a6e 35%,#2a7c8a 60%,#1a3d63 100%)}
.content{position:absolute;left:58px;right:58px;font-size:7px;line-height:1.55}
.page--one .content{top:260px}
.page--two .content{top:194px}
.content p{margin-bottom:5px;text-align:justify}
.content ul{list-style:none;margin:0 0 4px 0}
.content li{position:relative;padding-left:9px;margin-bottom:4px}
.content li::before{content:"";position:absolute;left:1px;top:3.5px;width:3px;height:3px;border-radius:50%;background:var(--ink)}
.section-head{color:var(--purple);font-weight:600;font-size:11.5px;line-height:1.2;margin:7px 0 4px}
.outcome{position:relative;padding-left:48px;margin-top:6px}
.outcome svg{position:absolute;left:0;top:2px}
.outcome .section-head{margin-top:0}
.footer-band{position:absolute;left:0;bottom:0;width:100%;height:80px}
.footer-label{position:absolute;right:22px;bottom:14px;color:#b9bbd8;font-size:7px;letter-spacing:.6px}
</style>
</head>
<body>

<section class="page page--one">
  <div class="masthead"></div>
  <svg class="accent" style="top:88px" width="536" height="30" viewBox="0 0 536 30">
    <polygon points="0,10 536,0 536,24 0,30" fill="var(--purple-soft)"/>
    <polygon points="0,8 536,0 536,4 0,12" fill="var(--teal)"/>
  </svg>
  <h1 class="page-title">How does a Vanilla Option contract work?</h1>
  <div class="hero" role="img" aria-label="Photo of a hand drawing a rising financial chart beside a laptop"></div>

  <div class="content">
    <p>The buyer of a vanilla option receives protection against an adverse movement in the exchange rate while allowing full participation in a beneficial move. At no time is the buyer of a Vanilla Option obligated to exercise the Option and transact the currencies, therefore providing flexibility in cases where the requirement to purchase foreign currency is not certain.</p>
    <p>A buyer of vanilla options is required to pay a premium (like an insurance premium) for the right, but not the obligation, to exchange currency at a predetermined rate on a predetermined date.</p>
    <ul>
      <li>Set a protection rate which will be your worst-case scenario at expiry</li>
      <li>Determine the amount of currency you wish to protect</li>
      <li>Choose an expiry date for the contract</li>
      <li>Calculate the premium you are required to pay</li>
    </ul>
    <h2 class="section-head">Let’s look at an example: You are in importer.</h2>
    <p>Your construction company has bid on a project that if successful, will require you to import materials from the United States to use in construction. You have used todays pricing of materials in calculating your bid and want to protect against an adverse move in the US dollar exchange rate from eroding your margin if your bid is chosen for the project.</p>
    <p>You choose to buy a Vanilla Call which will protect you from a rise in the USD/CAD exchange rate above your protection rate. You choose to buy protection on $500,000 USD, with a protection rate (strike rate) of 1.3300 expiring 3 months from now. You are required to pay a premium which in this case is calculated to be 1.8%, or 11,970 CAD.</p>

    <div class="outcome">
      <svg width="38" height="38" viewBox="0 0 38 38" aria-hidden="true">
        <circle cx="18" cy="20" r="15" fill="none" stroke="var(--purple)" stroke-width="3"/>
        <path d="M10 19 L17 26 L34 5" fill="none" stroke="var(--purple)" stroke-width="4" stroke-linecap="round" stroke-linejoin="round"/>
      </svg>
      <h2 class="section-head">Your bid is successful:</h2>
      <p>If the exchange rate is below your protection rate at expiration, you have no obligation relating to the vanilla call and you are free to buy USD at the cheaper spot rate. If the exchange rate is above your protection rate, your have the right to purchase your USD at the protection rate, and thereby claiming your insurance policy.</p>
    </div>
    <div class="outcome">
      <svg width="38" height="38" viewBox="0 0 38 38" aria-hidden="true">
        <circle cx="18" cy="20" r="15" fill="none" stroke="var(--alert)" stroke-width="3"/>
        <path d="M10 12 L26 28 M26 12 L10 28" fill="none" stroke="var(--alert)" stroke-width="4" stroke-linecap="round"/>
      </svg>
      <h2 class="section-head">Your bid is not successful:</h2>
      <p>You have no obligation relating to the vanilla option however, if at expiry the exchange rate is above the protection rate, you may exercise your right to buy USD at the lower rate and simultaneous sell USD back at the prevailing spot rate, thereby recouping some or all of the premium paid to buy the option. Alternatively, if you find out your bid was not successful with time still left until expiration, you may sell your option back into the market in the case that it still has residual value, which will depend on various market factors.</p>
    </div>
  </div>

  <svg class="footer-band" width="536" height="80" viewBox="0 0 536 80" aria-hidden="true">
    <polygon points="0,48 536,22 536,80 0,80" fill="var(--purple)"/>
    <polygon points="0,52 536,18 536,22 0,56" fill="var(--teal)"/>
    <polygon points="0,56 536,38 536,80 0,80" fill="var(--navy)"/>
  </svg>
  <div class="footer-label">VANILLA CONTRACTS | 1</div>
</section>

<section class="page page--two">
  <div class="masthead"></div>
  <svg class="accent" style="top:54px" width="536" height="20" viewBox="0 0 536 20">
    <polygon points="0,4 536,0 536,20 0,20" fill="var(--purple-soft)"/>
    <polygon points="0,10 536,6 536,12 0,16" fill="var(--teal)"/>
  </svg>
  <div class="hero" role="img" aria-label="Photo of a stock market ticker display with figures and green arrows"></div>

  <div class="content">
    <h2 class="section-head">Characteristics</h2>
    <ul>
      <li>You are looking for a straight-forward hedging solution</li>
      <li>You want to receive full benefit from an appreciation of the currency you are exposed to</li>
      <li>You are comfortable receiving protection at the strike rate of the option</li>
      <li>You are willing to pay the non-refundable premium</li>
    </ul>
    <h2 class="section-head">Advantages</h2>
    <ul>
      <li>You hedge your foreign currency exposure at a predefined hedge rate</li>
      <li>You can choose the hedge rate that suits your budget requirements</li>
      <li>Provides the ability to fully participate in a favourable exchange rate move</li>
      <li>You can choose from most major currency pairs to meet your needs</li>
    </ul>
    <h2 class="section-head">Risks</h2>
    <ul>
      <li>Premium paid is non-refundable and remains your only obligation when buying vanilla options</li>
    </ul>
    <h2 class="section-head">Why use Vanilla Options?</h2>
    <p>Vanilla options are often compared to an insurance product. The buyer pays a non-refundable premium for the right, but not the obligation to trade currency in the future at the protection rate of the option. This product allows you to participate in a beneficial move to an unlimited extent, which will be the most advantageous outcome, if the exchange rate moves in your favour enough to more than offset the premium paid for the option.</p>
    <h2 class="section-head">What determines the price of a Vanilla Option?</h2>
    <p>The cost of an option is defined by the premium that is required to be paid in order to enter into the contract. Premiums are calculated using the industry standard formulas based upon the Black Scholes model. The most important variables in the option pricing formulas include the following:</p>
    <ul>
      <li>The current market Spot Rate.</li>
      <li>Market volatility – the higher the volatility, the higher the premium.</li>
      <li>The Term of the Option – a longer term typically results in a higher premium.</li>
      <li>The Strike Rate – the closer to being ITM the protection rate is, the higher the premium.</li>
      <li>The interest rate differential of the two currencies involved.</li>
      <li>Style – European or American, or whether the option can be exercised prior to expiration</li>
    </ul>
    <p>An option can either a European (meaning that they can only be exercised on the expiry date), or American (meaning that they can be exercised at any time prior to expiration). We normally deals in European options however, we do offer American options under certain circumstances and when specific delivery terms are agreed upon between us and the customer.</p>
  </div>

  <svg class="footer-band" width="536" height="80" viewBox="0 0 536 80" aria-hidden="true">
    <polygon points="0,48 536,22 536,80 0,80" fill="var(--purple)"/>
    <polygon points="0,52 536,18 536,22 0,56" fill="var(--teal)"/>
    <polygon points="0,56 536,38 536,80 0,80" fill="var(--navy)"/>
  </svg>
  <div class="footer-label">VANILLA CONTRACTS | 2</div>
</section>

</body>
</html>
```